Industrial / automotive service company
Renewing and reconditioning solutions
Simple
Ted Pelkin
VP - Industrial Division
217 Marston Crescent NW
Calgary, Alberta
T2P 4G6
t-pelkin@zorvamail.com

```html
<!DOCTYPE html>
<html lang="en">
<head>
<meta charset="UTF-8">
<title>Tovalmex Services Inc. – Business Card</title>
<link href="https://fonts.googleapis.com/css2?family=Open+Sans:wght@400;600;700&display=swap" rel="stylesheet">
<style>
  :root {
    --lime: #8cc63f;
    --grey: #9a9ca0;
    --grey-dark: #5c5e62;
    --paper: #ffffff;
    --backdrop: #eceef0;
  }
  * { box-sizing: border-box; margin: 0; padding: 0; }
  html, body {
    width: 1200px; height: 874px; overflow: hidden;
    background: var(--backdrop);
    font-family: "Open Sans", Arial, sans-serif;
  }
  .sheet {
    width: 1200px; height: 874px;
    display: flex; align-items: center; justify-content: center; gap: 60px;
  }
  .card {
    position: relative;
    width: 540px; height: 310px;
    border-radius: 22px;
    overflow: hidden;
    box-shadow: 0 10px 28px rgba(0,0,0,0.12);
  }
  .card svg.decor { position: absolute; inset: 0; }

  /* Front */
  .card-front { background: var(--paper); }
  .brand {
    position: absolute; left: 70px; top: 70px;
    display: flex; align-items: center; gap: 10px;
  }
  .brand-dot {
    width: 18px; height: 18px; border-radius: 50%;
    background: var(--lime);
  }
  .brand-name {
    font-size: 24px; font-weight: 700; color: var(--lime);
    letter-spacing: 0.5px; line-height: 1.05;
  }
  .person {
    position: absolute; left: 236px; top: 140px;
    font-size: 9px; font-variant: small-caps; letter-spacing: 0.6px;
    text-align: center;
  }
  .person-name { color: var(--lime); font-weight: 600; font-size: 10px; }
  .person-title { color: var(--grey-dark); margin-top: 2px; }
  .details {
    position: absolute; left: 150px; top: 180px;
    display: flex; gap: 10px;
    font-size: 8.5px; color: var(--grey-dark); font-variant: small-caps;
    letter-spacing: 0.4px; line-height: 1.55;
  }
  .address {
    font-style: normal; text-align: right;
    padding-right: 10px; border-right: 1px solid var(--grey);
  }
  .contact-line { display: flex; align-items: center; gap: 5px; }
  .contact-line svg { width: 8px; height: 8px; fill: var(--lime); flex: none; }

  /* Back */
  .card-back { background: var(--lime); }
  .back-brand {
    position: absolute; left: 150px; top: 138px;
    display: flex; align-items: center; gap: 12px;
  }
  .back-dot {
    width: 22px; height: 22px; border-radius: 50%;
    background: var(--paper);
  }
  .back-name { font-size: 24px; font-weight: 700; color: var(--paper); }
  .web {
    position: absolute; right: 34px; bottom: 38px;
    font-size: 10px; color: var(--paper); font-variant: small-caps;
    letter-spacing: 1.2px;
  }
</style>
</head>
<body>
<main class="sheet">
  <section class="card card-front" aria-label="Business card front">
    <svg class="decor" viewBox="0 0 540 310" aria-hidden="true">
      <path d="M400 0 C440 30 500 34 540 18 L540 0 Z" fill="var(--lime)"/>
      <path d="M0 262 C90 236 180 290 310 310 L0 310 Z" fill="var(--lime)"/>
      <path d="M0 244 C100 218 190 278 330 306" fill="none" stroke="var(--grey)" stroke-width="5" stroke-linecap="round"/>
      <path d="M370 310 C440 296 500 255 540 205 L540 310 Z" fill="var(--lime)"/>
      <path d="M355 306 C435 290 498 246 540 190" fill="none" stroke="var(--grey)" stroke-width="4"/>
    </svg>
    <div class="brand">
      <span class="brand-dot"></span>
      <span class="brand-name">Tovalmex<br>Services Inc.</span>
    </div>
    <div class="person">
      <p class="person-name">Ted Pelkin</p>
      <p class="person-title">VP - Industrial Division</p>
    </div>
    <div class="details">
      <address class="address">
        217 Marston Crescent NW<br>
        Calgary, Alberta<br>
        T2P 4G6
      </address>
      <div class="contact">
        <p class="contact-line">
          <svg viewBox="0 0 10 10"><path d="M2 0h2l1 3-1.5 1a6 6 0 0 0 2.5 2.5L7 5l3 1v2a2 2 0 0 1-2 2A8 8 0 0 1 0 2a2 2 0 0 1 2-2z"/></svg>
          (403) 555-0187
        </p>
        <p class="contact-line">
          <svg viewBox="0 0 10 10"><path d="M0 2h10v6H0z M0 2l5 4 5-4" fill="none" stroke="var(--lime)" stroke-width="1.2"/></svg>
          t-pelkin@zorvamail.com
        </p>
        <p class="contact-line">
          <svg viewBox="0 0 10 10"><circle cx="5" cy="5" r="4.3" fill="none" stroke="var(--lime)" stroke-width="1.2"/></svg>
          www.tovalmexservices.com
        </p>
      </div>
    </div>
  </section>

  <section class="card card-back" aria-label="Business card back">
    <div class="back-brand">
      <span class="back-dot"></span>
      <span class="back-name">Tovalmex</span>
    </div>
    <p class="web">www.tovalmexservices.com</p>
  </section>
</main>
</body>
</html>
```